Wine Label Logo NEW name too

We would like to see this done in more colors but, lighter ones too. the dark colors don't show up that well. Can you also do some on white wine and not just red wine?

Also, we aren't sure we will use the name Plumvelle and wonder if you could use the name Nutmeadow with the same design to see how that looks, as well?

new wine label for a brand called Plumvelle (one word) and is targeted to go after 21-40 year olds. Probably more women than men. There will be Plumvelle Red, Plumvelle White, Plumvelle Cabernet, etc. the profile of the wine will be sweet...duh!!

would love you to come up with some TAG LINE ideas, as well. Size should be between 2 1/2 to 3 inches wide and 5 to 6 inches long. Needs place holders for varietal, Cabernet. 13.5% alcohol, area wil be California. I suggest you look at a bunch of wine labels to better understand this brief.

The final design should communicate fun, sweet, wine, young, hip

Wine labels matter. Period. Now, attempting to define “fun and contemporary” is nigh on impossible, but I think it would be safe to assume that this could mean “non-traditional.” Let’s face it. Design matters to millennial consumers. Quill, Tern Lodges, Hearthline Magazine – these brands are not ONLY for millennials by any means (well, maybe Tern), but design is top priority for these brands, and these brands have top priority for millennials. Feel free to do the math. If we spend money on something, we expect it to be beautiful and often times we expect social purchases like wine to act as a public reflection of our tastes and personality. This latter expectation is no different than any other generation (if arguably more intense due to our intrinsic personal branding tendencies); however, our personalities and what we are reflecting out to our peers IS different.
Updates

What about a label that is 2 1/2 to 3 inches wide and 5-6 inches long and looks like a white or off white piece of paper that has had berries poured across it with some stains and the name Plumvelle Cabernet as the logo on the label?  Needs space for the AVA area grown to say California and the vintage 2011 and alcohol level in small letters 12.3%. 

Look at some wine labels to get a unique idea. Needs to appeal to 21-40 year old women. Needs to denote the wine is sweet

Reason: two partners are out of the country and I want them involved in the choice

Target Market(s)

Industry/Entity Type

Social

Logo Text

Plumvelle Cabernet

Logo styles of interest
Pictorial/Combination Logo
Abstract Logo
Wordmark Logo

```html
<!DOCTYPE html>
<html lang="en">
<head>
<meta charset="utf-8">
<title>Plumvelle – Wine Labels</title>
<link rel="stylesheet" href="https://fonts.googleapis.com/css2?family=Italianno&family=Sorts+Mill+Goudy:ital@0;1&display=swap">
<style>
  :root {
    --stage-light: #ffffff;
    --stage-edge: #dcdcdc;
    --red-core: #cc2232;
    --red-edge: #8c0f1c;
    --red-rim: #a4162a;
    --red-shine: #e0707a;
    --red-motif: #b01826;
    --gold-core: #ebc067;
    --gold-edge: #a9661d;
    --gold-rim: #cf8c34;
    --gold-shine: #fbe2a6;
    --gold-motif: #c98a35;
    --ink-white: #ffffff;
    --ink-black: #111111;
    --crest-red: #7e0c17;
    --crest-gold: #b7582a;
  }
  html, body {
    margin: 0;
    width: 1200px;
    height: 801px;
    overflow: hidden;
  }
  body {
    background: radial-gradient(ellipse at 50% 45%, var(--stage-light) 55%, var(--stage-edge) 100%);
    position: relative;
  }
  .label {
    position: absolute;
    top: 119px;
    width: 466px;
    height: 593px;
  }
  .label--red { left: 52px; }
  .label--white { left: 681px; }
  .label svg { display: block; }
  .brand-name {
    font-family: "Italianno", cursive;
    font-size: 160px;
    fill: var(--ink-white);
    filter: drop-shadow(2px 4px 3px rgba(0,0,0,0.3));
  }
  .tagline {
    font-family: "Sorts Mill Goudy", serif;
    font-size: 31px;
    fill: var(--ink-black);
  }
  .sweetness {
    font-family: "Sorts Mill Goudy", serif;
    font-style: italic;
    font-size: 27px;
    fill: var(--ink-white);
  }
  .details {
    font-family: "Sorts Mill Goudy", serif;
    font-size: 23px;
    fill: var(--ink-white);
  }
  .details--year { font-size: 19px; letter-spacing: 1px; }
</style>
</head>
<body>

<div class="label label--red">
  <svg width="466" height="593" viewBox="0 0 466 593">
    <defs>
      <path id="label-shape" d="M40,8 Q233,-6 426,8 Q466,12 462,60 Q456,160 402,268 Q368,330 420,432 Q466,520 442,560 Q430,588 400,582 Q233,562 66,582 Q36,588 24,560 Q0,520 46,432 Q98,330 64,268 Q10,160 4,60 Q0,12 40,8 Z"/>
      <clipPath id="label-clip">
        <use href="#label-shape" transform="translate(10,9) scale(0.957,0.97)"/>
      </clipPath>
      <radialGradient id="red-fill" cx="50%" cy="55%" r="65%">
        <stop offset="0" stop-color="var(--red-core)"/>
        <stop offset="1" stop-color="var(--red-edge)"/>
      </radialGradient>
      <radialGradient id="red-motif" cx="50%" cy="50%" r="50%">
        <stop offset="0" stop-color="var(--red-motif)" stop-opacity="0.7"/>
        <stop offset="1" stop-color="var(--red-motif)" stop-opacity="0"/>
      </radialGradient>
    </defs>
    <use href="#label-shape" fill="var(--red-rim)"/>
    <use href="#label-shape" fill="url(#red-fill)" transform="translate(10,9) scale(0.957,0.97)"/>
    <g clip-path="url(#label-clip)">
      <ellipse role="img" aria-label="Faint leafy flourish ornament" cx="130" cy="150" rx="120" ry="130" fill="url(#red-motif)"/>
      <ellipse role="img" aria-label="Faint leafy flourish ornament" cx="130" cy="440" rx="110" ry="110" fill="url(#red-motif)"/>
    </g>
    <use href="#label-shape" fill="none" stroke="var(--red-shine)" stroke-width="3" opacity="0.8" transform="translate(24,22) scale(0.897,0.925)"/>
    <ellipse role="img" aria-label="Small crest ornament" cx="233" cy="45" rx="22" ry="26" fill="var(--crest-red)"/>
    <text class="brand-name" x="238" y="282" text-anchor="middle" textLength="290" lengthAdjust="spacingAndGlyphs">Plumvelle</text>
    <text class="tagline" x="232" y="318" text-anchor="middle">good mood wine</text>
    <text class="sweetness" x="233" y="418" text-anchor="middle">sweet</text>
    <text class="details" x="233" y="487" text-anchor="middle">Red Blend</text>
    <text class="details" x="233" y="518" text-anchor="middle">Paso Robles</text>
    <text class="details details--year" x="233" y="550" text-anchor="middle">2012</text>
  </svg>
</div>

<div class="label label--white">
  <svg width="466" height="593" viewBox="0 0 466 593">
    <defs>
      <radialGradient id="gold-fill" cx="55%" cy="55%" r="65%">
        <stop offset="0" stop-color="var(--gold-core)"/>
        <stop offset="1" stop-color="var(--gold-edge)"/>
      </radialGradient>
      <radialGradient id="gold-motif" cx="50%" cy="50%" r="50%">
        <stop offset="0" stop-color="var(--gold-motif)" stop-opacity="0.7"/>
        <stop offset="1" stop-color="var(--gold-motif)" stop-opacity="0"/>
      </radialGradient>
    </defs>
    <use href="#label-shape" fill="var(--gold-rim)"/>
    <use href="#label-shape" fill="url(#gold-fill)" transform="translate(10,9) scale(0.957,0.97)"/>
    <g clip-path="url(#label-clip)">
      <ellipse role="img" aria-label="Faint leafy flourish ornament" cx="120" cy="150" rx="110" ry="120" fill="url(#gold-motif)"/>
      <ellipse role="img" aria-label="Faint leafy flourish ornament" cx="160" cy="420" rx="140" ry="130" fill="url(#gold-motif)"/>
    </g>
    <use href="#label-shape" fill="none" stroke="var(--gold-shine)" stroke-width="3" opacity="0.9" transform="translate(24,22) scale(0.897,0.925)"/>
    <ellipse role="img" aria-label="Small crest ornament" cx="233" cy="45" rx="22" ry="26" fill="var(--crest-gold)"/>
    <text class="brand-name" x="238" y="282" text-anchor="middle" textLength="290" lengthAdjust="spacingAndGlyphs">Plumvelle</text>
    <text class="tagline" x="232" y="318" text-anchor="middle">good mood wine</text>
    <text class="sweetness" x="233" y="418" text-anchor="middle">sweet</text>
    <text class="details" x="233" y="490" text-anchor="middle">White Blend</text>
    <text class="details" x="233" y="521" text-anchor="middle">The Name</text>
    <text class="details details--year" x="233" y="553" text-anchor="middle">2012</text>
  </svg>
</div>

</body>
</html>
```